M25 Billboard Advert Required Please

I need an advert for a motorway Billboard on the M25 , the advert should show the following in big letters:
GUTTER CLEANING
DALRYNFLUES.COM and a small logo off to the side (Our logo is attached)

The printer has requested the following (Important please) the advert has to be
pdf file / 300 dpi/landscape orientation / scaled to a minimum 25% advert size ( this particular site is 22ft x 10ft so 25% of this please). Please also make sure that the artwork is embedded and outlined correctly if this is incorrect it will affect the printing of the banner.

Target Market(s)

General Public

Industry/Entity Type

Gutter Cleaning

Requirements
Should not have
• No Change to our Logo

```html
<!DOCTYPE html>
<html lang="en">
<head>
<meta charset="utf-8">
<title>Gutter Cleaning Billboard – Dalryn Flues</title>
<link rel="stylesheet" href="https://fonts.googleapis.com/css2?family=Barlow:wght@600;700;800&display=swap">
<style>
  :root {
    --page-bg: #e0e0e0;
    --band-white: #ffffff;
    --brand-red: #e30613;
    --ink: #111111;
    --headline: #ffffff;
    --headline-shadow: #2a1a0f;
    --photo-green: #5f6b3b;
    --photo-olive: #7b7650;
    --photo-brown: #6f4d33;
    --photo-deep: #4c3322;
    --photo-edge: #a08d58;
  }
  html, body {
    margin: 0;
    width: 1003px;
    height: 1200px;
    overflow: hidden;
    background: var(--page-bg);
  }
  .billboard {
    position: absolute;
    left: 41px;
    top: 391px;
    width: 920px;
    height: 418px;
    display: block;
  }
  .headline {
    font-family: "Barlow", sans-serif;
    font-weight: 800;
    fill: var(--headline);
  }
  .headline-shadow {
    font-family: "Barlow", sans-serif;
    font-weight: 800;
    fill: var(--headline-shadow);
  }
  .web-address {
    font-family: "Barlow", sans-serif;
    font-weight: 700;
    font-size: 55px;
    fill: var(--ink);
  }
  .web-address .web-name { fill: var(--brand-red); }
  .brand-name {
    font-family: "Barlow", sans-serif;
    font-weight: 700;
    font-size: 29px;
    fill: var(--ink);
  }
  .brand-tagline {
    font-family: "Barlow", sans-serif;
    font-weight: 600;
    font-size: 11.5px;
    fill: var(--ink);
  }
</style>
</head>
<body>
  <svg class="billboard" viewBox="0 0 920 418" xmlns="http://www.w3.org/2000/svg">
    <defs>
      <linearGradient id="scene-tones" x1="0" y1="0" x2="1" y2="0">
        <stop offset="0" stop-color="var(--photo-green)"/>
        <stop offset="0.2" stop-color="var(--photo-olive)"/>
        <stop offset="0.38" stop-color="var(--photo-deep)"/>
        <stop offset="0.6" stop-color="var(--photo-brown)"/>
        <stop offset="0.86" stop-color="var(--photo-brown)"/>
        <stop offset="1" stop-color="var(--photo-edge)"/>
      </linearGradient>
      <linearGradient id="scene-fade" x1="0" y1="0" x2="0" y2="1">
        <stop offset="0.55" stop-color="#1e120a" stop-opacity="0"/>
        <stop offset="1" stop-color="#1e120a" stop-opacity="0.75"/>
      </linearGradient>
    </defs>

    <g class="hero-photo" role="img" aria-label="Photo of a worker in a blue cap and red gloves cleaning a roof gutter beside a ladder, trees behind">
      <rect x="0" y="0" width="920" height="330" fill="url(#scene-tones)"/>
      <rect x="0" y="0" width="920" height="330" fill="url(#scene-fade)"/>
    </g>

    <g class="headline-group">
      <text class="headline-shadow" x="282" y="167" font-size="178" textLength="601" lengthAdjust="spacingAndGlyphs">GUTTER</text>
      <text class="headline" x="278" y="163" font-size="178" textLength="601" lengthAdjust="spacingAndGlyphs">GUTTER</text>
      <text class="headline-shadow" x="282" y="285" font-size="145" textLength="604" lengthAdjust="spacingAndGlyphs">CLEANING</text>
      <text class="headline" x="278" y="281" font-size="145" textLength="604" lengthAdjust="spacingAndGlyphs">CLEANING</text>
    </g>

    <rect class="info-band" x="0" y="330" width="920" height="88" fill="var(--band-white)"/>

    <text class="web-address" x="38" y="399" textLength="498" lengthAdjust="spacingAndGlyphs"><tspan class="web-name">DALRYNFLUES</tspan>.COM</text>

    <rect class="band-divider" x="614" y="343" width="2" height="62" fill="var(--brand-red)"/>

    <g class="brand-lockup">
      <rect x="683" y="358" width="14" height="14" fill="var(--brand-red)"/>
      <text class="brand-name" x="705" y="379" textLength="173" lengthAdjust="spacingAndGlyphs">Dalryn Flues</text>
      <text class="brand-tagline" x="683" y="402" textLength="195" lengthAdjust="spacingAndGlyphs">Clean gutters protect your property</text>
    </g>
  </svg>
</body>
</html>
```